A Flyer for a clinic/hospital waiting room to warn about patients that they must not abuse our staff

we need a flyer (text attached) with a background of a female nurse or medical doctor photo. I like the example photo where there are four headless satff lined up - something like this, indicating that we are a team and will not tolerate abuse
A4
the text will be over the photo.

Target Market(s)

patients who come to our clinic

Industry/Entity Type

medicine - urology

Colors
0054AA
0677BA
7BADD7
CADEEF
E8F1F8
0094D4
00A9DD
6FCCEA
C7EBF8
E9F6FB

Requirements
Must have
• a photo taking up the whole A4, and text over this. The photos I haev sent are just examples - I will need yo to source a photo
Nice to have
• Horizontal A4 and vertical A4 options. Please add our logo in small , in the bottom right corner

```html
<!DOCTYPE html>
<html lang="en">
<head>
<meta charset="utf-8">
<title>Riverbend Urology – Zero-Tolerance Flyer</title>
<link rel="stylesheet" href="https://fonts.googleapis.com/css2?family=Poppins:wght@400;500;600;700&display=swap">
<style>
  :root {
    --stage: #8c8c8e;
    --paper: #ffffff;
    --ink: #4a4a4c;
    --ink-soft: #5a5a5e;
    --brand-blue: #4f93d2;
    --band-blue: #5a9ed8;
    --band-blue-deep: #4a8ccb;
    --mist: #eef1f4;
    --charcoal: #48494d;
    --charcoal-deep: #3a3b3f;
    --white: #ffffff;
  }
  * { box-sizing: border-box; margin: 0; padding: 0; }
  html, body {
    width: 911px; height: 1200px; overflow: hidden;
    background: var(--stage);
    font-family: "Poppins", sans-serif;
  }
  .flyer {
    position: absolute; left: 31px; top: 0;
    width: 849px; height: 1200px;
    background: var(--paper); overflow: hidden;
  }
  .hero-photo {
    position: absolute; left: 0; top: 0; width: 849px; height: 576px;
    background: linear-gradient(90deg, #ffffff 0%, #f6f7f9 38%, #dfe5eb 58%, #5d9ad4 74%, #3a82c6 88%, #2f76bb 100%);
  }
  .brand {
    position: absolute; left: 49px; top: 128px;
    display: flex; align-items: center; gap: 10px;
  }
  .brand-dot { width: 30px; height: 30px; border-radius: 50%; background: var(--brand-blue); }
  .brand-name { font-size: 30px; font-weight: 500; color: var(--ink); letter-spacing: -0.5px; }

  .headline { position: absolute; left: 47px; top: 214px; color: var(--ink); }
  .headline .plain { display: block; font-size: 41px; font-weight: 400; line-height: 50px; padding-left: 8px; }
  .headline .tag {
    display: inline-block; background: var(--brand-blue); color: var(--white);
    font-size: 45px; font-weight: 700; line-height: 53px; padding: 0 14px 0 8px; letter-spacing: -0.5px;
  }
  .headline .tag-slant { clip-path: polygon(0 0, 95% 0, 100% 100%, 0 100%); padding-right: 44px; }
  .headline .gap-a { margin-bottom: 2px; }

  .subline {
    position: absolute; left: 49px; top: 432px;
    font-size: 29px; font-weight: 500; line-height: 36px; color: var(--ink);
  }

  .rules-band {
    position: absolute; left: 0; top: 576px; width: 849px; height: 280px;
    background: linear-gradient(90deg, var(--band-blue-deep) 0%, var(--band-blue) 60%, #5fa3dc 100%);
  }
  .rules-tab {
    position: absolute; left: 63px; top: 558px; width: 725px; height: 48px;
    background: linear-gradient(180deg, #55565b, var(--charcoal-deep));
    border-radius: 0 0 22px 22px;
    color: var(--white); font-size: 21px; font-weight: 600;
    display: flex; align-items: center; justify-content: center;
  }
  .tab-fold { position: absolute; top: 558px; }
  .rules-list {
    position: absolute; top: 638px; list-style: none;
    color: var(--white); font-size: 23px; font-weight: 500; line-height: 27px;
  }
  .rules-list.left { left: 82px; width: 300px; }
  .rules-list.right { left: 453px; width: 330px; }
  .rules-list li { position: relative; padding-left: 27px; margin-bottom: 6px; }
  .rules-list li::before {
    content: ""; position: absolute; left: 0; top: 9px;
    width: 11px; height: 11px; border-radius: 50%;
    background: var(--white); border: 3px solid var(--charcoal);
  }

  .support-area {
    position: absolute; left: 0; top: 856px; width: 849px; height: 187px;
    background: linear-gradient(180deg, #f4f5f7, var(--mist) 60%, #f7f8fa);
  }
  .support-box {
    position: absolute; left: 53px; top: 890px; width: 367px; height: 111px;
    border: 2px solid var(--brand-blue); border-radius: 12px; background: var(--white);
    padding: 8px 0 0 12px;
    color: var(--brand-blue); font-size: 21px; font-weight: 700; line-height: 28px;
  }
  .consequence {
    position: absolute; left: 449px; top: 898px; width: 380px;
    color: var(--ink-soft); font-size: 18px; line-height: 23px;
  }

  .footer-band {
    position: absolute; left: 0; top: 1043px; width: 849px; height: 157px;
    background: var(--charcoal); color: var(--white); padding: 24px 40px 0 46px;
  }
  .footer-band .lead { font-size: 17.5px; font-weight: 600; line-height: 21px; }
  .footer-band .reason { font-size: 17.5px; font-weight: 400; line-height: 21px; margin-top: 12px; }
</style>
</head>
<body>
  <main class="flyer">
    <div class="hero-photo" role="img" aria-label="Photo of medical staff in blue scrubs and white coats with stethoscopes, arms crossed, faded to white on the left"></div>

    <div class="brand">
      <span class="brand-dot"></span>
      <span class="brand-name">Riverbend Urology</span>
    </div>

    <h1 class="headline">
      <span class="plain">We have</span>
      <span class="tag gap-a">Zero-tolerance</span>
      <span class="plain">for any form of</span>
      <span class="tag tag-slant">Aggressive behaviour</span>
    </h1>

    <p class="subline">Our staff treat you with respect<br>and we expect the same in return</p>

    <section class="rules-band" aria-hidden="true"></section>
    <svg class="tab-fold" style="left:51px" width="14" height="14" viewBox="0 0 14 14"><polygon points="14,0 14,14 0,14" fill="#222"/></svg>
    <svg class="tab-fold" style="left:786px" width="14" height="14" viewBox="0 0 14 14"><polygon points="0,0 0,14 14,14" fill="#222"/></svg>
    <h2 class="rules-tab">Aggressive behaviour (in-person or on the telephone) is:</h2>

    <ul class="rules-list left">
      <li>Verbal harassment</li>
      <li>Any verbal or physical confrontation</li>
      <li>Raising your voice or making unreasonable demands</li>
    </ul>
    <ul class="rules-list right">
      <li>Abusive or intimidating behaviour</li>
      <li>Sexual or suggestive language or behaviour</li>
      <li>Making threats to our staff</li>
      <li>Swearing</li>
    </ul>

    <section class="support-area" aria-hidden="true"></section>
    <p class="support-box">If any of our staff feel<br>intimidated in any way,<br>we will always support them.</p>
    <p class="consequence">Incidents will result in your immediate removal from the facility, termination of your relationship with the practice, and may result in prosecution.</p>

    <footer class="footer-band">
      <p class="lead">In all circumstances we will support any staff member who wishes to press charges against a perpetrator of aggressive behaviour.</p>
      <p class="reason">We take this stance because our staff work extremely hard in busy circumstances to help you and we will no longer tolerate any form of aggression or abuse.</p>
    </footer>
  </main>
</body>
</html>
```